Penwick Insurance Post Card

Specializing in “Towing & Transportation Insurance”
See our website at http://penwickins-example.net/ for ideas on colors fonts etc.

Target Market(s)

Towing Companies

Font styles to use
Serif
Sans Serif

Requirements
Must have
• Specializing in “Towing & Transportation Insurance”
• Welcome to Penwick Insurance:
• 2nd sentence (With our Agency, we work to make ourselves available to your business for when you need us most to keep your business moving forward.)
• 3rd Sentence: (Our customers were in mind when developing our agency and will continue to find new ways to make doing business with us easier.)
• We Offer: Change “Dealers Physical Damage” to “Auto Dealer Liability” & “Garage Liability” to “Garage Repair Liability”
• Our address: 418 5th St NW, Suite B Decatur, AL 35602
• Email Address: PenwickInfo@velmorlink.example

```html
<!DOCTYPE html>
<html lang="en">
<head>
<meta charset="utf-8">
<title>Penwick Insurance Post Card</title>
<link href="https://fonts.googleapis.com/css2?family=Oswald:wght@400;500;600;700&family=Open+Sans:ital,wght@0,400;0,600;0,700;1,400;1,600&display=swap" rel="stylesheet">
<style>
  :root {
    --navy: #1c3a52;
    --navy-deep: #142c40;
    --navy-mid: #24475f;
    --gold: #8a6220;
    --gold-light: #d8b060;
    --white: #ffffff;
    --ink: #1f2a33;
    --line: #9aa3aa;
    --stage: #e6e6e4;
  }
  * { box-sizing: border-box; margin: 0; padding: 0; }
  html, body { width: 1200px; height: 960px; overflow: hidden; }
  body { background: var(--stage); font-family: "Open Sans", sans-serif; position: relative; }

  .card {
    position: absolute; left: 285px; width: 630px; height: 420px;
    overflow: hidden; box-shadow: 0 6px 18px rgba(0,0,0,.18);
  }
  .card--front { top: 40px; background: linear-gradient(180deg, var(--navy-mid), var(--navy) 40%, var(--navy-deep)); }
  .card--back { top: 500px; background: var(--white); }

  /* FRONT */
  .front-photo {
    position: absolute; left: 0; top: 52px; width: 350px; height: 266px;
    background: linear-gradient(160deg, #8a7a70 0%, #6b7d92 35%, #4c5d78 60%, #2b2f36 100%);
  }
  .front-photo__shade {
    position: absolute; inset: 0;
    background: linear-gradient(180deg, rgba(0,0,0,0) 45%, rgba(10,20,30,.75) 100%);
  }
  .headline {
    position: absolute; left: 12px; top: 212px; color: var(--white);
    font-family: "Oswald", sans-serif; font-weight: 600; font-size: 22px;
    line-height: 1.05; text-transform: uppercase; text-shadow: 0 1px 3px rgba(0,0,0,.6);
  }
  .gold-rule { position: absolute; left: 0; top: 318px; width: 630px; height: 4px; background: var(--gold); }
  .offer-panel { position: absolute; left: 0; top: 0; width: 630px; height: 420px; }
  .brand {
    position: absolute; left: 338px; top: 44px; width: 260px; text-align: center;
    font-family: "Oswald", sans-serif; font-weight: 500; font-size: 26px;
    color: var(--navy); letter-spacing: 2px; text-transform: uppercase;
  }
  .offer-title {
    position: absolute; left: 360px; top: 104px; width: 230px; text-align: center;
    font-family: "Oswald", sans-serif; font-weight: 700; font-size: 32px; color: var(--gold);
  }
  .offer-list {
    position: absolute; left: 375px; top: 168px; list-style: none;
    font-family: "Oswald", sans-serif; font-weight: 500; font-size: 18px; color: var(--ink);
  }
  .offer-list li { display: flex; align-items: center; gap: 7px; height: 32px; }
  .offer-list li::before {
    content: ""; width: 7px; height: 7px; border-radius: 50%;
    border: 2px solid var(--gold); background: var(--white);
  }
  .front-footer {
    position: absolute; left: 18px; top: 380px; display: flex; align-items: center;
    gap: 16px; color: var(--white);
  }
  .front-footer__call { font-family: "Oswald", sans-serif; font-size: 19px; font-weight: 400; }
  .front-footer__item { display: flex; align-items: center; gap: 6px; font-size: 14px; font-weight: 700; }
  .front-footer__sep { width: 1px; height: 18px; background: rgba(255,255,255,.6); }
  .social-dot { position: absolute; left: 582px; top: 388px; width: 16px; height: 16px; border-radius: 50%; background: var(--navy-mid); }

  /* BACK */
  .back-shape { position: absolute; left: 0; top: 0; width: 630px; height: 420px; }
  .back-brand {
    position: absolute; left: 24px; top: 16px;
    font-family: "Oswald", sans-serif; font-weight: 500; font-size: 24px;
    color: var(--navy); letter-spacing: 2px; text-transform: uppercase;
  }
  .back-copy {
    position: absolute; left: 24px; top: 70px; width: 340px;
    color: var(--white); font-size: 11.5px; font-weight: 600; line-height: 1.35;
  }
  .back-copy p + p { margin-top: 12px; }
  .testimonial {
    position: absolute; left: 24px; top: 194px; width: 340px;
    color: var(--gold-light); font-size: 10px; font-style: italic; line-height: 1.45;
    padding: 0 22px;
  }
  .testimonial__mark { position: absolute; font-family: "Oswald", sans-serif; font-size: 26px; font-style: normal; line-height: 1; color: var(--gold-light); }
  .testimonial__mark--open { left: 0; top: -2px; }
  .testimonial__mark--close { right: 0; bottom: -12px; }
  .testimonial__by {
    position: absolute; left: 200px; top: 282px; width: 140px; color: var(--gold-light);
    font-size: 10px; font-weight: 700; line-height: 1.2; text-align: right;
  }
  .contact {
    position: absolute; left: 24px; top: 340px;
    color: var(--white); font-size: 10px; font-weight: 600; line-height: 1.9;
  }
  .contact__row { display: flex; align-items: center; gap: 7px; }
  .contact__item { display: flex; align-items: center; gap: 5px; }
  .contact__sep { width: 1px; height: 11px; background: rgba(255,255,255,.6); }
  .address-lines { position: absolute; left: 420px; top: 40px; width: 190px; }
  .address-lines span { display: block; height: 1px; background: var(--line); margin-bottom: 26px; }
  .welcome {
    position: absolute; right: 22px; bottom: 52px; text-align: right;
    font-family: "Oswald", sans-serif; font-weight: 700; font-size: 17px;
    color: var(--gold); line-height: 1.1;
  }
</style>
</head>
<body>

<section class="card card--front" aria-label="Post card front">
  <div class="front-photo" role="img" aria-label="Photo of a damaged blue sedan strapped onto a flatbed tow truck on a city street">
    <div class="front-photo__shade"></div>
  </div>
  <h1 class="headline">Specializing in<br>Towing &amp; Transportation<br>Insurance</h1>
  <div class="gold-rule"></div>

  <svg class="offer-panel" viewBox="0 0 630 420" aria-hidden="true">
    <path d="M318 30 H610 V355 L478 372 L350 355 V92 H340 A22 22 0 0 1 318 70 Z" fill="#fbfbfa"/>
    <path d="M318 30 H610 V92 H340 A22 22 0 0 1 318 70 Z" fill="#ffffff"/>
    <line x1="378" y1="160" x2="590" y2="160" stroke="#1f2a33" stroke-width="1.2"/>
    <path d="M476 160 L484 167 L492 160" fill="none" stroke="#1f2a33" stroke-width="1.2"/>
  </svg>
  <div class="brand">Penwick Insurance</div>
  <h2 class="offer-title">WE OFFER</h2>
  <ul class="offer-list">
    <li>Auto Liability</li>
    <li>Auto Dealer Liability</li>
    <li>Garage Repair Liability</li>
    <li>Garagekeepers</li>
    <li>Wrongful Repossession</li>
  </ul>

  <div class="front-footer">
    <span class="front-footer__call">Call Now!</span>
    <span class="front-footer__item">
      <svg width="13" height="13" viewBox="0 0 24 24" aria-hidden="true"><path fill="#fff" d="M6.6 10.8a15 15 0 0 0 6.6 6.6l2.2-2.2a1 1 0 0 1 1-.25 11.4 11.4 0 0 0 3.6.57 1 1 0 0 1 1 1V20a1 1 0 0 1-1 1A17 17 0 0 1 3 4a1 1 0 0 1 1-1h3.5a1 1 0 0 1 1 1c0 1.25.2 2.45.57 3.57a1 1 0 0 1-.25 1z"/></svg>
      +334-555-0187
    </span>
    <span class="front-footer__sep"></span>
    <span class="front-footer__item">
      <svg width="13" height="13" viewBox="0 0 24 24" aria-hidden="true"><g fill="none" stroke="#fff" stroke-width="2"><circle cx="12" cy="12" r="9"/><path d="M3 12h18M12 3c3 3.5 3 14.5 0 18M12 3c-3 3.5-3 14.5 0 18"/></g></svg>
      penwickins-example.net
    </span>
  </div>
  <span class="social-dot" aria-hidden="true"></span>
</section>

<section class="card card--back" aria-label="Post card back">
  <svg class="back-shape" viewBox="0 0 630 420" aria-hidden="true">
    <path d="M0 56 H380 V220 L500 420 H0 Z" fill="#1c3a52"/>
    <path d="M380 0 V220 L500 420" fill="none" stroke="#8a6220" stroke-width="5"/>
  </svg>
  <div class="back-brand">Penwick Insurance</div>
  <div class="back-copy">
    <p>With our Agency, we work to make ourselves available to your business for when you need us most to keep your business moving forward.</p>
    <p>Our customers were in mind when developing our agency and will continue to find new ways to make doing business with us easier.</p>
  </div>
  <blockquote class="testimonial">
    <span class="testimonial__mark testimonial__mark--open">&ldquo;</span>
    We have been very pleased with Penwick Insurance. We have been in the trucking business for over 25 years and have found Penwick to be one of the most thorough, hands on, dependable insurance agencies we have ever delt with. They are a caring company that keeps their clients first. Cudos to Penwick, the best ever!
    <span class="testimonial__mark testimonial__mark--close">&rdquo;</span>
  </blockquote>
  <div class="testimonial__by">Dale Harmon<br>Auto Transporter</div>
  <div class="contact">
    <div class="contact__row">
      <span class="contact__item">
        <svg width="10" height="10" viewBox="0 0 24 24" aria-hidden="true"><path fill="#fff" d="M12 2a7 7 0 0 0-7 7c0 5 7 13 7 13s7-8 7-13a7 7 0 0 0-7-7zm0 9.5A2.5 2.5 0 1 1 12 6.5a2.5 2.5 0 0 1 0 5z"/></svg>
        Penwick Insurance, LLC, 418 5th St NW, Suite B Decatur, AL 35602
      </span>
    </div>
    <div class="contact__row">
      <span class="contact__item">
        <svg width="10" height="10" viewBox="0 0 24 24" aria-hidden="true"><path fill="#fff" d="M6.6 10.8a15 15 0 0 0 6.6 6.6l2.2-2.2a1 1 0 0 1 1-.25 11.4 11.4 0 0 0 3.6.57 1 1 0 0 1 1 1V20a1 1 0 0 1-1 1A17 17 0 0 1 3 4a1 1 0 0 1 1-1h3.5a1 1 0 0 1 1 1c0 1.25.2 2.45.57 3.57a1 1 0 0 1-.25 1z"/></svg>
        +334-555-0187
      </span>
      <span class="contact__sep"></span>
      <span class="contact__item">
        <svg width="11" height="9" viewBox="0 0 24 18" aria-hidden="true"><rect x="1" y="1" width="22" height="16" rx="2" fill="none" stroke="#fff" stroke-width="2"/><path d="M1 2l11 8 11-8" fill="none" stroke="#fff" stroke-width="2"/></svg>
        PenwickInfo@velmorlink.example
      </span>
      <span class="contact__sep"></span>
      <span class="contact__item">
        <svg width="10" height="10" viewBox="0 0 24 24" aria-hidden="true"><g fill="none" stroke="#fff" stroke-width="2"><circle cx="12" cy="12" r="9"/><path d="M3 12h18M12 3c3 3.5 3 14.5 0 18M12 3c-3 3.5-3 14.5 0 18"/></g></svg>
        penwickins-example.net
      </span>
    </div>
  </div>
  <div class="address-lines" aria-hidden="true"><span></span><span></span><span></span><span></span></div>
  <p class="welcome">Welcome to<br>Penwick Insurance</p>
</section>

</body>
</html>
```